Faithful Harbor Fellowship Network needs a fresh new web design

We are an up and coming multicultural church that aims to bring people into a life changing encounter with God. We need a fresh and inviting website in order to increase our internet presence and make us easier to connect with.
Here are some of the basic requirements for the site:
• Clearly displayed address, service times, and contact info
• A staff profile page
• An area for a calendar with upcoming events and their details
• Social media buttons
• Group pages for the different ministries (youth, children’s church, men, etc…)
• An area for donations and eCommerce
• A resources page for assorted media (podcasts, sermons, videos, etc.…)
• An area for prayer requests.

Industry/Entity Type

Church

```html
<!DOCTYPE html>
<html lang="en">
<head>
<meta charset="utf-8">
<title>Faithful Harbor Fellowship Network</title>
<link rel="stylesheet" href="https://fonts.googleapis.com/css2?family=Vollkorn:wght@400;600&family=Open+Sans:ital,wght@0,400;0,600;0,700;1,400&display=swap">
<style>
:root{
  --gold:#d9ad2a;
  --gold-light:#f3d56a;
  --bar:#b8942f;
  --bar-dark:#9c7b22;
  --ink:#3a2c0a;
  --text:#555;
  --purple:#240b78;
  --field:#1d1050;
  --footer:#2d2009;
  --footer-head:#d9a72c;
  --footer-text:#e8e0cc;
  --white:#fff;
}
*{box-sizing:border-box;margin:0;padding:0}
html,body{width:680px;height:1200px;overflow:hidden;background:var(--white)}
body{position:relative;font-family:"Open Sans",Arial,sans-serif;color:var(--text)}
.abs{position:absolute}

.masthead{left:0;top:0;width:680px;height:310px;background:radial-gradient(ellipse at 50% 15%,#fff2a8 0%,#f0c94a 35%,#d9a521 75%,#c48d18 100%)}
.brand{left:0;top:40px;width:680px;font-family:"Vollkorn",Georgia,serif;font-weight:600;font-size:17px;color:var(--purple);display:flex;justify-content:center;align-items:center;gap:8px}
.brand .dot{width:24px;height:24px;border-radius:50%;background:var(--purple)}
.hero{left:103px;top:101px;width:474px;height:159px;background:linear-gradient(180deg,#8e6f9c 0%,#c7889a 40%,#e6b08a 70%,#5a4530 100%)}
.hero-text{left:22px;top:68px}
.hero-text h2{font-family:"Vollkorn",Georgia,serif;font-weight:400;font-size:18px;color:var(--purple)}
.hero-text p{font-family:"Vollkorn",Georgia,serif;font-size:9px;color:#1b1b1b}
.hero-text .ref{color:#f3e6e6;margin-top:6px}
.dots{right:14px;bottom:8px;display:flex;gap:2px}
.dots span{width:9px;height:9px;border-radius:50%;background:#7a6a40;font-size:6px;color:#fff;text-align:center;line-height:9px}
.dots span.on{background:var(--gold)}
.nav{left:103px;top:260px;width:474px;height:31px;background:linear-gradient(#e9c24a,#c99d22);display:flex;box-shadow:0 6px 8px rgba(90,60,0,.35)}
.nav a{font-family:"Vollkorn",Georgia,serif;font-size:9.5px;color:#fff;text-decoration:none;padding:0 13px;line-height:31px;border-right:1px solid #d7b34a}

.welcome{left:103px;top:328px;width:295px}
.welcome h1{font-family:"Vollkorn",Georgia,serif;font-weight:400;font-size:15px;color:var(--ink);margin-bottom:8px}
.welcome p{font-size:6.5px;line-height:12px;margin-bottom:7px}
.welcome .hope{font-family:"Vollkorn",Georgia,serif;font-weight:400;font-size:8.5px;color:var(--ink);margin-top:10px}

.bar{height:28px;background:var(--bar);color:#fff;font-family:"Vollkorn",Georgia,serif;font-size:12px;line-height:28px;padding-left:8px}
.group{left:103px;top:498px;width:294px}
.select{position:absolute;right:5px;top:5px;width:94px;height:17px;background:#5c4410;font-size:6px;line-height:17px;padding-left:5px;color:var(--gold-light)}
.thumbs{display:flex;gap:5px;margin-top:5px}
.thumb{position:relative;width:95px;height:69px;background:linear-gradient(135deg,#c8b79a,#6d5a45)}
.thumb span{position:absolute;left:3px;bottom:4px;font-family:"Vollkorn",Georgia,serif;font-size:5.5px;color:#fff}
.thumb i{position:absolute;right:4px;bottom:3px;width:8px;height:8px;border-radius:50%;background:#fff}

.staff{left:103px;top:626px;width:294px}
.staff-photo{left:103px;top:670px;width:65px;height:85px;background:linear-gradient(180deg,#eef0f4,#4a4550)}
.staff-cap{left:103px;top:765px;width:65px;text-align:center;font-family:"Vollkorn",Georgia,serif;font-style:italic;font-size:8px;color:#777;line-height:10px}
.staff-cap b{display:block;font-family:"Open Sans",Arial,sans-serif;font-weight:400;font-size:6.5px;color:var(--bar-dark)}
.staff-bio{left:182px;top:664px;width:222px}
.staff-bio h3{font-family:"Vollkorn",Georgia,serif;font-weight:400;font-size:8.5px;color:var(--bar-dark);margin-bottom:6px}
.staff-bio p{font-size:6.3px;line-height:12px;color:#777;margin-bottom:8px}

.testi{left:103px;top:814px;width:294px;height:80px;background:var(--bar);padding:6px 8px}
.testi h3{font-family:"Vollkorn",Georgia,serif;font-weight:400;font-size:12px;color:#fff}
.testi .arrows{position:absolute;right:8px;top:6px;font-size:11px;color:var(--gold-light)}
.testi .q{font-family:"Vollkorn",Georgia,serif;font-size:26px;color:var(--gold-light);line-height:18px;height:12px}
.testi p{font-style:italic;font-size:6.3px;line-height:10.5px;color:#fff;padding-left:4px}

.cal{left:423px;top:334px;width:152px;height:267px;background:linear-gradient(#e2b33c,#d7a52c)}
.cal-head{height:24px;background:#3a2d10;display:flex;justify-content:space-between;align-items:center;padding:0 4px;color:var(--gold);font-size:7.5px;font-weight:700}
.cal-head i{width:9px;height:9px;background:#e8e0c8;color:#3a2d10;font-size:5px;font-style:normal;display:flex;align-items:center;justify-content:center}
.cal-grid{display:grid;grid-template-columns:repeat(7,1fr);padding:8px 4px 0;font-size:5.2px;text-align:center;color:#3a2d10}
.cal-grid span{height:17.6px;line-height:17.6px;border-bottom:1px solid #c99a28}
.cal-grid .wd{height:12px;line-height:12px;border:0}
.cal-ev{padding:6px 10px 0}
.cal-ev h4{font-size:6px;color:#2b2006;margin:6px 0 4px}
.ev{display:flex;gap:5px;padding-bottom:6px;margin-bottom:6px;border-bottom:1px solid #f0cf6c}
.ev-img{width:43px;height:30px;background:linear-gradient(135deg,#7b6f66,#2e2a2a);flex:none}
.ev p{font-size:5px;line-height:7.5px;color:#fff6d8}
.btn-dark{position:absolute;right:9px;bottom:8px;background:#2b2006;color:#fff;font-size:5.5px;padding:5px 7px}

.prayer{left:423px;top:619px;width:152px;height:275px;background:var(--purple);padding:10px 12px}
.prayer h3{font-family:"Vollkorn",Georgia,serif;font-weight:400;font-size:14px;color:var(--gold);margin-bottom:5px}
.prayer label{display:block;font-family:"Vollkorn",Georgia,serif;font-size:6.3px;line-height:8px;color:#fff;margin-bottom:5px}
.prayer .field{height:17px;background:var(--field);margin-bottom:9px}
.prayer .field.big{height:40px;margin-bottom:8px}
.submit{float:right;background:var(--gold);color:#fff;font-size:6.5px;font-weight:700;padding:4px 8px}

.motto{left:0;top:912px;width:680px;text-align:center;font-family:"Vollkorn",Georgia,serif;font-size:15px;color:var(--ink)}
.media{top:943px;width:155px;height:68px}
.media .label{position:absolute;left:8px;bottom:11px;font-family:"Vollkorn",Georgia,serif;font-size:12px;color:#fff}
.media .more{position:absolute;right:5px;bottom:12px;background:var(--purple);color:#fff;font-family:"Vollkorn",Georgia,serif;font-size:6px;padding:4px 6px}

.footer{left:0;top:1036px;width:680px;height:164px;background:var(--footer)}
.fcol{top:1050px}
.fcol h4{font-size:6.5px;line-height:9px;font-weight:700;color:var(--footer-head);margin-bottom:14px}
.fcol li{list-style:none;font-size:6.5px;color:var(--footer-text);line-height:12px}
.info{display:flex;align-items:center;gap:9px;font-size:6.5px;line-height:9px;color:var(--footer-text);margin-bottom:7px}
.info svg{flex:none}
.social{display:flex;gap:3px}
.social span{width:16px;height:16px;border-radius:50%;border:1px solid #8a6a20;background:#4a3a18}
.cards{display:flex;gap:5px;margin-top:4px}
.cards span{width:23px;height:12px;background:#f2f2f2;border-radius:1px}
.pill{width:80px;height:13px;background:var(--gold);border-radius:7px;margin-top:6px}
.legal{left:0;top:1160px;width:680px;text-align:center;font-size:6.5px;color:var(--footer-text);line-height:14px}
</style>
</head>
<body>

<header class="abs masthead" role="img" aria-label="Golden sunset sky above clouds"></header>
<div class="abs brand"><span class="dot"></span>Faithful Harbor Fellowship Network</div>

<section class="abs hero" role="img" aria-label="Silhouette of a man kneeling in prayer on a grassy hill at sunset">
  <div class="abs hero-text">
    <h2>Random Bible Verse</h2>
    <p>Set your affection on things above, not on things on the earth.</p>
    <p class="ref">Colossians 3:2</p>
  </div>
  <div class="abs dots"><span class="on">1</span><span>2</span><span>3</span><span>4</span></div>
</section>

<nav class="abs nav">
  <a href="#">Home</a><a href="#">About Us</a><a href="#">Events</a><a href="#">Prayer Request</a><a href="#">Donate</a><a href="#">Contact Us</a>
</nav>

<section class="abs welcome">
  <h1>Welcome to FHFN</h1>
  <p>Welcome to Faithful Harbor Fellowship Network, a place where we can come together and fellowship. FHFN is located in Riverton, New York and we would love to have you worship with us. We believe God is doing something extraordinary through our church and would like for you to be a part. Please prayerfully consider our church as a place you would like to worship and fellowship with us as we continue to grow.</p>
  <p>As you venture on our website please feel free to contact us through email, phone, or leave a prayer request for us to pray on your behalf. Please take a minute and look at our upcoming events.</p>
  <p class="hope">We hope you will visit us real soon.</p>
</section>

<section class="abs group">
  <div class="bar" style="position:relative">Group<span class="select">Children's Church</span></div>
  <div class="thumbs">
    <div class="thumb" role="img" aria-label="Children praying in church"><span>Childrens In church</span><i></i></div>
    <div class="thumb" role="img" aria-label="Children gathered in church pews"><span>Childrens In church</span><i></i></div>
    <div class="thumb" role="img" aria-label="Children seated in a church hall"><span>Childrens In church</span><i></i></div>
  </div>
</section>

<section class="abs staff"><div class="bar">Our Staffs</div></section>
<div class="abs staff-photo" role="img" aria-label="Portrait of the minister holding a Bible"></div>
<div class="abs staff-cap">Minister<b>Marisol Grant</b></div>
<div class="abs staff-bio">
  <h3>Marisol Grant-Minister, Sunday School Teacher</h3>
  <p>Marisol Grant is the co-founder of Faithful Harbor Fellowship Network. A native of Panama who accepted the Lord at the age of 19, she is a dedicated educator in both the secular and Christian community, helping children and adults with special needs acquire and achieve life long skills.</p>
  <p>Definitely, without the grace and help of the almighty God this work would not be possible. The goal of the educational ministry is to help children and young adults build their educational skills and spiritual walk with Christ.</p>
</div>

<section class="abs testi">
  <h3>Testimonials</h3><span class="arrows">&lsaquo;&rsaquo;</span>
  <div class="q">&ldquo;</div>
  <p>Lorem Ipsum is simply dummy text of the printing and typesetting industry. Lorem Ipsum has been the industry's standard dummy text ever since the 1500s, when an unknown printer took a galley of type and scrambled it to make a type specimen book</p>
</section>

<aside class="abs cal">
  <div class="cal-head"><i>&#9664;</i>Jun 2014<i>&#9654;</i></div>
  <div class="cal-grid">
    <span class="wd">Mon</span><span class="wd">Tue</span><span class="wd">Wed</span><span class="wd">Thu</span><span class="wd">Fri</span><span class="wd">Sat</span><span class="wd">Sun</span>
    <span>27</span><span>28</span><span>29</span><span>01</span><span>02</span><span>03</span><span>04</span>
    <span>05</span><span>06</span><span>07</span><span>08</span><span>09</span><span>10</span><span>11</span>
    <span>12</span><span>13</span><span>14</span><span>15</span><span>16</span><span>17</span><span>18</span>
    <span>19</span><span>20</span><span>21</span><span>22</span><span>23</span><span>24</span><span>25</span>
    <span>26</span><span>27</span><span>28</span><span>29</span><span>30</span><span>31</span><span></span>
  </div>
  <div class="cal-ev">
    <h4>Events Calendar</h4>
    <div class="ev"><div class="ev-img" role="img" aria-label="Congregation at an event"></div><p>Lorem Ipsum is simply dummy text of the printing and typesetting industry.</p></div>
    <div class="ev" style="border:0"><div class="ev-img" role="img" aria-label="Worship service on stage"></div><p>Lorem Ipsum is simply dummy text of the printing and typesetting industry.</p></div>
  </div>
  <span class="btn-dark">Read More</span>
</aside>

<aside class="abs prayer">
  <h3>Prayer Requests</h3>
  <label>Your Name:</label><div class="field"></div>
  <label>Your Email Address:</label><div class="field"></div>
  <label>Prayer Title:</label><div class="field"></div>
  <label>Prayer Topic:</label><div class="field"></div>
  <label>Your Prayer Request:</label><div class="field big"></div>
  <span class="submit">SUBMIT</span>
</aside>

<p class="abs motto">"No limits, No Boundaries, but increase in Jesus name"</p>

<div class="abs media" style="left:103px;background:linear-gradient(135deg,#5a6a70,#1a2226 60%,#6fc8c0)" role="img" aria-label="Studio microphone">
  <span class="label">Podcasts</span><span class="more">Read More</span></div>
<div class="abs media" style="left:263px;background:linear-gradient(135deg,#3a3a3a,#6b5a48 50%,#222)" role="img" aria-label="Hands holding an open Bible">
  <span class="label">Sermons</span><span class="more">Read More</span></div>
<div class="abs media" style="left:422px;background:linear-gradient(135deg,#c98a4a,#f4d9a0 45%,#7a4a2a)" role="img" aria-label="Cross against a glowing sunset">
  <span class="label">Videos</span><span class="more">Read More</span></div>

<footer class="abs footer"></footer>
<div class="abs fcol" style="left:103px">
  <h4>Home Links</h4>
  <ul><li>Home</li><li>About Us</li><li>Events</li><li>Prayer Request</li><li>Donate</li><li>Contact Us</li></ul>
</div>
<div class="abs fcol" style="left:248px">
  <h4>Contact Info, Address &amp; Time</h4>
  <div class="info"><svg width="9" height="9" viewBox="0 0 10 10"><rect x="1" y="1" width="8" height="8" rx="1" fill="none" stroke="#e8e0cc"/><rect x="3" y="3" width="4" height="2" fill="#e8e0cc"/></svg>555.013.4821</div>
  <div class="info"><svg width="9" height="9" viewBox="0 0 10 10"><rect x="1" y="1.5" width="8" height="5.5" fill="none" stroke="#e8e0cc"/><path d="M3 9h4" stroke="#e8e0cc"/></svg>www.faithfulharbor.org</div>
  <div class="info"><svg width="9" height="9" viewBox="0 0 10 10"><path d="M5 9.5C2.5 6 2 5 2 4a3 3 0 0 1 6 0c0 1-.5 2-3 5.5z" fill="#e8e0cc"/></svg>2240 Harbor Lane Riverton NY 11500</div>
  <div class="info"><svg width="9" height="9" viewBox="0 0 10 10"><circle cx="5" cy="5.5" r="3.8" fill="none" stroke="#e8e0cc"/><path d="M5 3.5v2.2l1.4.9" stroke="#e8e0cc" fill="none"/></svg>9.00am -12.00am (Admission $20.00)</div>
</div>
<div class="abs fcol" style="left:420px">
  <h4>Connect With US</h4>
  <div class="social"><span></span><span></span><span></span><span></span><span></span></div>
  <h4 style="margin:10px 0 4px">Payment options</h4>
  <div class="cards"><span></span><span></span><span></span></div>
  <div class="pill"></div>
</div>
<p class="abs legal">Privacy Policy | Terms Conditions | Sitemap | Contact Us<br>&copy; 2012 FHFN. All Rights Reserved</p>

</body>
</html>
```